Korvell Plant Services

We are a heavy diesel mechanical business with additional air con certificates, remapping engine rebuilt

Contact Information for Business Card

Company Name, Director Name, Managing Director, Contact details, email and website

Font styles to use
Serif
Script

```html
<!DOCTYPE html>
<html lang="en">
<head>
<meta charset="utf-8">
<title>Korvell Plant Services – Business Card</title>
<link rel="stylesheet" href="https://fonts.googleapis.com/css2?family=Playfair+Display:wght@700&family=Great+Vibes&family=Poppins:wght@300&display=swap">
<style>
  :root {
    --backdrop: #d3d4cf;
    --card-white: #ffffff;
    --navy: #17147a;
    --ink: #2b2b2b;
    --charcoal: #2f2f30;
    --charcoal-deep: #262627;
    --edge: #1d1c8a;
  }
  * { box-sizing: border-box; margin: 0; padding: 0; }
  html, body {
    width: 1200px; height: 801px; overflow: hidden;
    background: var(--backdrop);
    font-family: "Poppins", sans-serif;
  }
  .stage {
    position: relative; width: 1200px; height: 801px;
    display: flex; align-items: center; justify-content: center; gap: 40px;
  }
  .card {
    position: relative; width: 540px; height: 308px;
    border-bottom: 4px solid var(--edge);
    box-shadow: 0 12px 24px rgba(0,0,0,0.18);
    overflow: hidden;
  }
  .card--front { background: var(--card-white); }
  .card--back { background: var(--charcoal); }

  .brand {
    position: absolute; left: 52px; top: 44px;
    display: flex; align-items: center; gap: 12px;
  }
  .brand__dot {
    width: 48px; height: 48px; border-radius: 50%;
    background: var(--navy);
  }
  .brand__name {
    font-family: "Playfair Display", serif; font-weight: 700;
    font-size: 22px; line-height: 1.1; color: var(--navy);
    width: 170px;
  }

  .contact {
    position: absolute; left: 100px; bottom: 48px; width: 210px;
    font-size: 12px; font-weight: 300; color: var(--ink); line-height: 1.35;
  }
  .contact__address { margin-bottom: 8px; }
  .contact__row { display: flex; align-items: center; gap: 7px; }
  .contact__row svg { width: 10px; height: 10px; flex: none; }
  .contact__web { color: var(--navy); }

  .person {
    position: absolute; right: 34px; bottom: 46px; text-align: right;
  }
  .person__name {
    font-family: "Playfair Display", serif; font-weight: 700;
    font-size: 21px; letter-spacing: 0.8px; color: var(--navy); line-height: 1.1;
  }
  .person__role {
    font-family: "Great Vibes", cursive;
    font-size: 20px; color: var(--ink); line-height: 1.1; margin-top: 2px;
  }

  .rule {
    position: absolute; left: 100px; right: 34px; bottom: 30px;
    height: 2px; background: var(--navy);
  }

  .pattern-field {
    position: absolute; inset: 0;
    background: linear-gradient(135deg, var(--charcoal) 0%, var(--charcoal-deep) 100%);
  }
  .back-brand {
    position: absolute; right: 34px; bottom: 90px;
    display: flex; align-items: center; gap: 6px;
  }
  .back-brand__dot { width: 14px; height: 14px; border-radius: 50%; background: var(--card-white); }
  .back-brand__name {
    font-family: "Playfair Display", serif; font-weight: 700;
    font-size: 12px; color: var(--card-white);
  }
</style>
</head>
<body>
<main class="stage">
  <section class="card card--front" aria-label="Business card front">
    <div class="brand">
      <span class="brand__dot"></span>
      <span class="brand__name">Korvell Plant Services</span>
    </div>

    <div class="contact">
      <p class="contact__address">1720 Ridgeline Rd<br>Millbrook, GA 30412</p>
      <p class="contact__row">
        <svg viewBox="0 0 12 12"><path d="M2.5 1l2 2.5-1 1.2c.6 1.3 1.5 2.2 2.8 2.8l1.2-1 2.5 2-1.2 1.5C5 9.5 2.5 7 1 2.2z" fill="#17147a"/></svg>
        470-555-0148
      </p>
      <p class="contact__row">
        <svg viewBox="0 0 12 12"><rect x="1" y="2.5" width="10" height="7" fill="none" stroke="#17147a" stroke-width="1.2"/><path d="M1 2.5l5 4 5-4" fill="none" stroke="#17147a" stroke-width="1.2"/></svg>
        info@korvellplant.com
      </p>
      <p class="contact__row contact__web">
        <svg viewBox="0 0 12 12"><circle cx="6" cy="6" r="5" fill="#17147a"/><path d="M1 6h10M6 1v10" stroke="#fff" stroke-width="0.7"/></svg>
        www.korvellplant.com
      </p>
    </div>

    <div class="person">
      <p class="person__name">DANIEL HARTWELL</p>
      <p class="person__role">Director</p>
    </div>

    <div class="rule"></div>
  </section>

  <section class="card card--back" aria-label="Business card back">
    <div class="pattern-field" role="img" aria-label="Tone-on-tone repeating brand pattern in dark charcoal"></div>
    <div class="back-brand">
      <span class="back-brand__dot"></span>
      <span class="back-brand__name">Korvell Plant Services</span>
    </div>
  </section>
</main>
</body>
</html>
```